Need a stunning home page for Car rental company

For a client, I need a slick and sumber home page design. It is a small, local car rental company, with a handful of cars available for rent.
Selling points: affordable lease, availability, always clean cars
The design should be:
- flat and modern
- no, or very few animations/sliders
- CTA: booking form for renting a car.
- 3 featured cars with images and facts (see website) with button to read more about the car.
- fullscreen background video can be an option
- main colour: #efba01
The site is under construction here:
http://tormesbil.ulvenkor.no/
Delivery requirements:
I need a layered & well organised PSD file delivered.

```html
<!DOCTYPE html>
<html lang="no">
<head>
<meta charset="utf-8">
<title>Tormes Bilutleie</title>
<link href="https://fonts.googleapis.com/css2?family=Open+Sans:wght@400;600;700&display=swap" rel="stylesheet">
<style>
:root{
  --brand:#efba01;
  --brand-dark:#d9a600;
  --ink:#2b2b2b;
  --muted:#6d6d6d;
  --line:#d8d8d8;
  --card:#ececec;
  --dark:#222222;
  --white:#ffffff;
}
*{box-sizing:border-box;margin:0;padding:0}
html,body{width:744px;height:1200px;overflow:hidden;background:var(--white);font-family:"Open Sans",sans-serif;color:var(--ink)}
.page{position:relative;width:744px;height:1200px}
.abs{position:absolute}

.site-header{left:0;top:0;width:744px;height:63px;background:var(--white)}
.brand{left:112px;top:20px;font-size:17px;font-weight:700;color:var(--dark);letter-spacing:1px;display:flex;align-items:center;gap:6px}
.brand-dot{width:10px;height:10px;background:var(--brand);border-radius:50%}
.lang{left:615px;top:13px;width:10px;height:7px;background:#3a4c9a;border:1px solid #c33}
.call{left:430px;top:38px;font-size:8px;color:var(--muted)}
.call strong{font-size:10px;color:var(--ink);font-weight:600}
.search{left:519px;top:31px;width:113px;height:24px;border:1px solid var(--line);font-size:7px;color:#999;padding:7px 6px}
.search svg{position:absolute;right:6px;top:8px}

.main-nav{left:0;top:63px;width:744px;height:33px;background:linear-gradient(#f2c11c,var(--brand-dark))}
.main-nav a{position:absolute;top:13px;font-size:7px;color:var(--dark);text-decoration:none;text-transform:uppercase}
.login{left:562px;top:63px;width:70px;height:33px;background:var(--dark);color:var(--white);font-size:7px;text-align:center;line-height:33px}

.hero{left:0;top:96px;width:744px;height:294px;background:linear-gradient(100deg,#5a5f5c 0%,#9ca29c 35%,#7d7f7a 55%,#a4271f 72%,#4c4a47 100%)}
.booking{left:112px;top:119px;width:219px;height:252px;background:var(--white);padding:15px 17px;box-shadow:0 1px 4px rgba(0,0,0,.3)}
.booking h2{font-size:12px;font-weight:400;margin-bottom:4px}
.booking label{display:block;font-size:6px;color:var(--muted);text-transform:uppercase;margin-bottom:4px}
.field{height:25px;border:1px solid var(--line);font-size:6px;color:#aaa;padding:8px 10px;margin-bottom:10px;position:relative}
.pair{display:flex;gap:8px}
.pair .field{flex:1}
.btn{display:block;background:linear-gradient(#f2c11c,var(--brand-dark));color:#3a3a3a;text-align:center;text-transform:uppercase;font-size:10px;height:29px;line-height:29px}
.caption{left:372px;top:304px;width:260px;height:67px;background:rgba(255,255,255,.85);padding:10px 7px;text-align:right;font-size:9.5px;line-height:16px;color:#444}

.welcome{left:0;top:390px;width:744px;height:119px;background:var(--brand);text-align:center;padding:15px 110px}
.welcome h1{font-size:13px;font-weight:400;margin-bottom:8px}
.welcome p{font-size:6px;line-height:16px;color:#3b3b3b}

.offers-title{left:0;top:526px;width:744px;text-align:center;font-size:13px}
.car{top:550px;width:166px;height:350px;background:var(--card);box-shadow:0 8px 8px -6px rgba(0,0,0,.35)}
.car-img{height:97px;background:linear-gradient(#dcdcdc,#f2f2f2)}
.car-body{padding:8px 12px}
.car h3{font-size:9.5px;font-weight:400;padding-bottom:7px;border-bottom:1px solid var(--line);margin-bottom:3px}
.spec{display:flex;font-size:7px;height:19.2px;align-items:center;color:var(--muted)}
.spec span:first-child{width:111px}
.spec span:last-child{color:var(--ink)}
.spec.first{border-bottom:1px solid var(--line);height:22px;margin-bottom:2px}
.car .btn{margin:11px 1px 0;height:34px;line-height:34px;font-size:9px}
.car .rule{border-top:1px solid var(--line);margin-top:4px}

.video{left:0;top:930px;width:744px;height:227px;background:linear-gradient(90deg,#2c3236,#4d5256 50%,#2b2f33)}
.play{left:344px;top:1019px}

.site-footer{left:0;top:1157px;width:744px;height:43px;background:var(--dark)}
.copy{left:112px;top:1176px;font-size:7px;color:#aaa}
.social{left:540px;top:1173px;display:flex;gap:4px}
.social i{width:12px;height:12px;border-radius:50%;display:block}
</style>
</head>
<body>
<div class="page">
  <header class="abs site-header"></header>
  <div class="abs brand"><span>TORMES BILUTLEIE</span><span class="brand-dot"></span></div>
  <div class="abs lang"></div>
  <div class="abs call">Call Now : <strong>40123456</strong></div>
  <div class="abs search">Search...
    <svg width="7" height="7" viewBox="0 0 10 10"><circle cx="4" cy="4" r="3" fill="none" stroke="#aaa" stroke-width="1.4"/><path d="M6.5 6.5 9 9" stroke="#aaa" stroke-width="1.4"/></svg>
  </div>

  <nav class="abs main-nav">
    <a style="left:119px">Home</a>
    <a style="left:174px">Services</a>
    <a style="left:239px">Vehicle Models</a>
    <a style="left:333px">Reviews</a>
    <a style="left:396px">Locations</a>
    <a style="left:470px">Contact</a>
  </nav>
  <div class="abs login">LOGIN</div>

  <section class="abs hero" role="img" aria-label="Red sports sedan speeding along a mountain road"></section>
  <form class="abs booking">
    <h2>BOOK A CAR</h2>
    <label>Location</label>
    <div class="field">Enter City or Airport....</div>
    <label>Car Type</label>
    <div class="field">Select
      <svg style="position:absolute;right:9px;top:10px" width="7" height="5" viewBox="0 0 8 5"><path d="M0 0 4 4 8 0" fill="none" stroke="#999"/></svg>
    </div>
    <label>Pick Up</label>
    <div class="pair"><div class="field">Date</div><div class="field">Time</div></div>
    <label>Drop-Off</label>
    <div class="pair"><div class="field">Date</div><div class="field">Time</div></div>
    <span class="btn">Book Now</span>
  </form>
  <div class="abs caption">Lorem ipsum dolor sit amet, consectetuer adipiscing elit, sed diam nonummyvolutpat.
    <div style="margin-top:4px">
      <svg width="22" height="8" viewBox="0 0 22 8"><path d="M8 4H1M4 1 1 4l3 3M14 4h7M18 1l3 3-3 3" fill="none" stroke="#777" stroke-width="2"/></svg>
    </div>
  </div>

  <section class="abs welcome">
    <h1>Velkommen til Tormes Bilutleie – Ulvenvik</h1>
    <p>Ut wisi enim ad minim veniam, quis nostrud exerci tation ullamcorper suscipit lobortis nisl ut aliquip ex ea commodo consequat. Duis autem vel eum iriure dolor in hendrerit in vulputate velit esse molestie consequat, vel illum dolore eu feugiat nulla facilisis at vero eros et accumsan et iusto odio dignissim qui blandit praesent luptatum zzril delenit augue duis dolore te feugait nulla facilisi. Nam liber tempor cum soluta nobis eleifend option congue nihil imperdiet doming id quod mazim placerat facer possim assum</p>
  </section>

  <h2 class="abs offers-title" style="font-weight:400">Våre leietilbud</h2>

  <article class="abs car" style="left:112px">
    <div class="car-img" role="img" aria-label="Black compact SUV"></div>
    <div class="car-body">
      <h3>Varebilen</h3>
      <div class="spec first"><span>Pris per døgn</span><span>kr 600</span></div>
      <div class="spec"><span>Biltype</span><span>Varebil</span></div>
      <div class="spec"><span>Maks. pers</span><span>2</span></div>
      <div class="spec"><span>Ant. dører</span><span>5</span></div>
      <div class="spec"><span>Min. sjåføralder</span><span>21</span></div>
      <div class="spec"><span>Girtype</span><span>Manuell</span></div>
      <div class="spec"><span>Klimaanlegg?</span><span>Ja</span></div>
      <div class="spec"><span>Ubegrenset km?</span><span>Nei</span></div>
      <div class="rule"></div>
      <span class="btn">Read More</span>
    </div>
  </article>
  <article class="abs car" style="left:288px">
    <div class="car-img" role="img" aria-label="Silver family sedan"></div>
    <div class="car-body">
      <h3>Lorem ipsum dolo</h3>
      <div class="spec first"><span>Pris per døgn</span><span>kr 600</span></div>
      <div class="spec"><span>Biltype</span><span>Varebil</span></div>
      <div class="spec"><span>Maks. pers</span><span>2</span></div>
      <div class="spec"><span>Ant. dører</span><span>5</span></div>
      <div class="spec"><span>Min. sjåføralder</span><span>21</span></div>
      <div class="spec"><span>Girtype</span><span>Manuell</span></div>
      <div class="spec"><span>Klimaanlegg?</span><span>Ja</span></div>
      <div class="spec"><span>Ubegrenset km?</span><span>Nei</span></div>
      <div class="rule"></div>
      <span class="btn">Read More</span>
    </div>
  </article>
  <article class="abs car" style="left:464px">
    <div class="car-img" role="img" aria-label="White compact crossover"></div>
    <div class="car-body">
      <h3>Varebilen</h3>
      <div class="spec first"><span>Pris per døgn</span><span>kr 600</span></div>
      <div class="spec"><span>Biltype</span><span>Varebil</span></div>
      <div class="spec"><span>Maks. pers</span><span>2</span></div>
      <div class="spec"><span>Ant. dører</span><span>5</span></div>
      <div class="spec"><span>Min. sjåføralder</span><span>21</span></div>
      <div class="spec"><span>Girtype</span><span>Manuell</span></div>
      <div class="spec"><span>Klimaanlegg?</span><span>Ja</span></div>
      <div class="spec"><span>Ubegrenset km?</span><span>Nei</span></div>
      <div class="rule"></div>
      <span class="btn">Read More</span>
    </div>
  </article>

  <section class="abs video" role="img" aria-label="Video still: dark luxury sedan driving through a city street"></section>
  <svg class="abs play" width="48" height="48" viewBox="0 0 48 48" aria-label="Play video">
    <circle cx="24" cy="24" r="23" fill="#b3262a"/>
    <path d="M19 15v18l14-9z" fill="#e6e6e6"/>
  </svg>

  <footer class="abs site-footer"></footer>
  <div class="abs copy">© Tormes Bilutleie 2014. All rights reserved.</div>
  <div class="abs social">
    <i style="background:#3b5998"></i><i style="background:#2aa9e0"></i><i style="background:#1a78b4"></i><i style="background:#d23a2e"></i><i style="background:#f26522"></i><i style="background:#dc4a38"></i>
  </div>
</div>
</body>
</html>
```